New Business Cards for NYC Salon

We are updating all of our cards. 7142-2869-4057 is my account number. We put names of our stylists on their cards. The back should include appointment space. Were looking for something more sleek and modern. Black/White Silver... or even touches of the orange color on our website which has been our thing for years. The design should communicate professional upscale boutique salon for men and women. Should be able to incorporate design into thank you cards, referral cards, brochure and postcards. The file is a zip file...we like the stacked ones black or white or the side versions.

Industry/Entity Type

Beauty Salon

Contact Information for Business Card

Marcus John's Salon313 W. 53rd Street, New York NY 10019 212-386-7714 info@marcusdellsalon.example www.marcusdellsalon.example

Font styles to use
Other font styles liked:
• trajan

Requirements
Must have
• we print a different card for every person in the salon. Begin by designing with the name Marcus. We will change it with every employee when printing. Must have a space for appointment date and time.
Nice to have
• Were looking to move towards the stacked or side placed logo but not opposed to utilizing the circular.
Should not have
• Photos

```html
<!DOCTYPE html>
<html lang="en">
<head>
<meta charset="utf-8">
<title>Marcus Dell's Salon – Business Card</title>
<link rel="stylesheet" href="https://fonts.googleapis.com/css2?family=Cinzel:wght@500&family=Open+Sans:wght@400&display=swap">
<style>
  :root {
    --orange: #ef7d00;
    --ink: #1f1f1f;
    --muted: #6a6a6a;
    --white: #ffffff;
    --band: #f1f1f1;
    --band-alt: #ebebeb;
    --stripe-grey: #b9b9b9;
    --ornament-grey: #a9a9a9;
    --rule: #9a9a9a;
    --frame: #d4d4d4;
  }
  * { margin: 0; padding: 0; box-sizing: border-box; }
  html, body {
    width: 1200px; height: 704px; overflow: hidden; background: var(--white);
  }
  .card {
    position: relative; width: 1200px; height: 704px;
    background: var(--white); border: 2px solid var(--frame); overflow: hidden;
  }
  .card__art { position: absolute; inset: 0; }
  .ornament-area {
    position: absolute; left: 860px; top: 0; width: 340px; height: 360px;
    background: radial-gradient(ellipse at 75% 30%, var(--ornament-grey) 0%, #c8c8c8 45%, rgba(255,255,255,0) 78%);
  }
  .salon-name {
    position: absolute; left: 36px; top: 140px;
    font-family: "Cinzel", serif; font-weight: 500;
    font-size: 55px; line-height: 1; letter-spacing: 1px; color: var(--orange); white-space: nowrap;
  }
  .salon-address {
    position: absolute; left: 36px; top: 206px;
    font-family: "Open Sans", sans-serif; font-size: 38px; line-height: 1.2; color: var(--ink); white-space: nowrap;
  }
  .appointment {
    position: absolute; left: 36px; top: 318px;
    display: flex; align-items: flex-end; gap: 14px;
    font-family: "Open Sans", sans-serif; font-size: 24px; line-height: 1; color: var(--muted); white-space: nowrap;
  }
  .appointment__field { display: inline-block; border-bottom: 2px solid var(--rule); height: 24px; }
  .appointment__field--date { width: 190px; }
  .appointment__field--time { width: 150px; }
  .brand-mark {
    position: absolute; left: 20px; top: 512px; width: 270px;
    text-align: center; font-family: "Cinzel", serif; font-weight: 500;
    font-size: 30px; line-height: 1.3; letter-spacing: 3px; color: var(--white);
  }
  .contact {
    position: absolute; right: 148px;
    font-family: "Open Sans", sans-serif; line-height: 1;
    color: var(--ink); text-align: right; white-space: nowrap;
  }
  .contact--phone { top: 444px; font-size: 48px; }
  .contact--email { top: 548px; font-size: 44px; }
  .contact--web { top: 606px; font-size: 44px; }
  .icon { position: absolute; }
  .icon--phone { left: 1060px; top: 426px; width: 86px; height: 86px; }
  .icon--computer { left: 1074px; top: 562px; width: 80px; height: 90px; }
</style>
</head>
<body>
<main class="card">
  <svg class="card__art" width="1200" height="704" viewBox="0 0 1200 704" aria-hidden="true">
    <rect class="band band--phone" x="0" y="403" width="1200" height="128" fill="var(--band)"/>
    <rect class="band band--online" x="0" y="536" width="1200" height="132" fill="var(--band-alt)"/>
    <polygon class="stripe stripe--grey" points="420,668 688,668 710,704 444,704" fill="var(--stripe-grey)"/>
    <polygon class="stripe stripe--orange" points="688,668 953,668 975,704 710,704" fill="var(--orange)"/>
    <polygon class="stripe stripe--grey" points="953,668 1200,668 1200,704 975,704" fill="var(--stripe-grey)"/>
    <polygon class="brand-panel" points="0,403 257,403 444,704 0,704" fill="var(--orange)"/>
  </svg>

  <div class="ornament-area" role="img" aria-label="Decorative flowing hair swirl ornament in grey"></div>

  <h1 class="salon-name">Marcus Dell's Salon</h1>
  <p class="salon-address">748 E. 29th Street, New York NY</p>

  <p class="appointment">
    <span>Appointment&nbsp;&nbsp;Date</span><span class="appointment__field appointment__field--date"></span>
    <span>Time</span><span class="appointment__field appointment__field--time"></span>
  </p>

  <p class="brand-mark">Marcus Dell's<br>Salon</p>

  <p class="contact contact--phone">10016 212-386-7714</p>
  <svg class="icon icon--phone" viewBox="0 0 86 86" aria-hidden="true">
    <path d="M6,30 C6,12 80,12 80,30 L80,36 L62,36 L62,28 L24,28 L24,36 L6,36 Z" fill="var(--orange)"/>
    <path d="M22,36 L64,36 L80,58 L80,80 L6,80 L6,58 Z" fill="var(--orange)"/>
    <g fill="var(--white)">
      <rect x="30" y="46" width="6" height="5"/><rect x="40" y="46" width="6" height="5"/><rect x="50" y="46" width="6" height="5"/>
      <rect x="30" y="55" width="6" height="5"/><rect x="40" y="55" width="6" height="5"/><rect x="50" y="55" width="6" height="5"/>
      <rect x="30" y="64" width="6" height="5"/><rect x="40" y="64" width="6" height="5"/><rect x="50" y="64" width="6" height="5"/>
    </g>
  </svg>

  <p class="contact contact--email">info@marcusdellsalon.example</p>
  <p class="contact contact--web">www.marcusdellsalon.example</p>
  <svg class="icon icon--computer" viewBox="0 0 80 90" aria-hidden="true">
    <rect x="6" y="4" width="68" height="56" rx="3" fill="var(--orange)"/>
    <rect x="13" y="11" width="54" height="42" fill="var(--white)"/>
    <rect x="18" y="16" width="44" height="32" fill="var(--orange)"/>
    <polygon points="6,64 74,64 80,86 0,86" fill="var(--orange)"/>
    <g fill="var(--white)">
      <rect x="10" y="69" width="60" height="3"/><rect x="8" y="75" width="64" height="3"/><rect x="20" y="81" width="40" height="2"/>
    </g>
  </svg>
</main>
</body>
</html>
```